New Cryotherapy Business needs a Flyer Design

We are expanding our massage business located in Sydney with a Cryosauna. We need a flyer/brochure that explain what whole body cryotherapy is and all its benefits in a very simple way as we are the first cryotherapy business in Sydney and not many people knows what it is yet. We would like to see a design that use the color of our logo or shades of blue that comunicate freshness, innovation and health but also movement and sport performance. The flyer targets gym's members, athletes and also yoga/pilates goers with a focus on wellbeing and health.

Please find attached our logo (we actually prefer to use the logo/font in the banner adding the hand underneath the vitruvian man) and some examples of cryotherapy flyers with the information about the product/service we would like to include in the flyer. We would like also to include a section with special offer for new clients.

Target Market(s)

The flyer targets gym's members, athletes and also yoga/pilates goers with a focus on wellbeing and health.

Industry/Entity Type

Health And Wellness

Font styles to use
Sans Serif

Colors
f78f20
848484
c3c3c3
85acd3
0792cd
3176b5

Requirements
Must have
• logo, contact details, FAQs, About WBC, Benefits, Applications include, special offer for new clients section, pic of cryosauna with muscular guy, logos of "as seen on tv"

```html
<!DOCTYPE html>
<html lang="en">
<head>
<meta charset="utf-8">
<title>Whole Body Cryotherapy Brochure</title>
<link href="https://fonts.googleapis.com/css2?family=Montserrat:wght@400;500;600;700;800&display=swap" rel="stylesheet">
<style>
  :root {
    --blue-main: #0792cd;
    --blue-bright: #23aef0;
    --blue-ink: #1a63b0;
    --blue-offer: #1a86d6;
    --orange: #f7a520;
    --text-dark: #3c3c3c;
    --white: #ffffff;
    --badge-ring: #9dc6e6;
    --logo-ink: #1d3f6e;
  }
  * { margin: 0; padding: 0; box-sizing: border-box; }
  html, body { width: 1200px; height: 904px; overflow: hidden; background: #f4f4f4; }
  .brochure {
    position: relative; width: 1200px; height: 904px;
    display: grid; grid-template-columns: 402px 403px 395px;
    font-family: "Montserrat", Arial, sans-serif;
  }
  .panel { position: relative; height: 904px; overflow: hidden; }

  /* About panel */
  .panel--about {
    background: linear-gradient(180deg, var(--blue-bright) 0%, var(--blue-main) 55%, #1aa4e6 100%);
    color: var(--white);
  }
  .about-photo {
    position: absolute; left: 150px; top: 640px; width: 252px; height: 264px;
    background: radial-gradient(ellipse at 40% 30%, rgba(255,255,255,0.18), rgba(255,255,255,0.04) 70%);
  }
  .about-head { position: absolute; left: 30px; top: 42px; width: 340px; }
  .about-head h1 { font-weight: 700; font-size: 28px; line-height: 34px; letter-spacing: 0.5px; }
  .about-head h2 {
    font-weight: 700; font-size: 20.5px; line-height: 24px; padding-bottom: 10px;
    border-bottom: 1px solid rgba(255,255,255,0.7);
  }
  .about-body {
    position: absolute; left: 30px; top: 124px; width: 340px;
    font-size: 13px; font-weight: 500; line-height: 22.8px;
  }
  .pill {
    position: absolute; left: 0; height: 37px; width: 336px;
    background: var(--orange); border-radius: 0 19px 19px 0;
    font-weight: 700; font-size: 17.5px; line-height: 37px;
    padding-left: 30px; letter-spacing: 0.3px; color: var(--white);
  }
  .pill--benefits { top: 429px; }
  .pill--applications { top: 593px; }
  .bullets { position: absolute; list-style: none; font-size: 13px; font-weight: 500; line-height: 21.3px; }
  .bullets li { padding-left: 16px; position: relative; }
  .bullets li::before {
    content: ""; position: absolute; left: 0; top: 7px; width: 8px; height: 8px;
    border: 1.4px solid var(--white); border-radius: 50%;
  }
  .bullets--benefits-a { left: 30px; top: 482px; }
  .bullets--benefits-b { left: 204px; top: 482px; }
  .bullets--applications { left: 30px; top: 645px; }

  /* FAQ panel */
  .panel--faq {
    background: linear-gradient(90deg, #e2e2e2 0%, #f6f6f6 8%, #ffffff 20%);
    color: var(--text-dark);
  }
  .faq-title { position: absolute; left: 14px; top: 52px; display: flex; align-items: center; width: 372px; }
  .faq-title h2 { font-weight: 700; font-size: 48px; line-height: 56px; color: var(--blue-ink); letter-spacing: -0.5px; }
  .faq-title span { flex: 1; height: 5px; background: var(--blue-ink); margin-left: 10px; margin-top: 6px; }
  .faq-item { position: absolute; left: 14px; width: 370px; }
  .faq-item--work { top: 117px; }
  .faq-item--safe { top: 339px; }
  .faq-item--comfort { top: 531px; }
  .faq-item--after { top: 680px; }
  .faq-item h3 { font-weight: 700; font-size: 17px; color: var(--blue-main); line-height: 21.5px; margin-bottom: 2px; }
  .faq-item p { font-size: 13px; font-weight: 500; line-height: 21.3px; }

  /* Offer panel */
  .panel--offer { background: var(--white); }
  .tv-banner { position: absolute; left: 37px; top: 43px; width: 319px; height: 50px; }
  .tv-banner svg { position: absolute; inset: 0; }
  .tv-banner span {
    position: relative; display: block; text-align: center; line-height: 50px;
    font-weight: 700; font-size: 29px; color: var(--white);
  }
  .tv-logos {
    position: absolute; left: 24px; top: 142px; width: 346px;
    display: flex; justify-content: space-between; align-items: center;
  }
  .tv-logos--row2 { top: 216px; padding: 0 10px; }
  .tv-name {
    display: flex; align-items: center; gap: 5px;
    font-weight: 700; font-size: 13px; color: var(--logo-ink);
  }
  .tv-name i { display: block; width: 11px; height: 11px; background: var(--logo-ink); }
  .cryo-photo {
    position: absolute; left: 0; top: 283px; width: 395px; height: 307px;
    background: linear-gradient(135deg, #f5f5f5 0%, #e3e6ea 40%, #b9bec6 70%, #8f969f 100%);
  }
  .offer-block {
    position: absolute; left: 0; top: 590px; width: 395px; height: 314px;
    background: linear-gradient(180deg, var(--blue-offer) 0%, var(--blue-main) 100%);
    color: var(--white); text-align: center;
  }
  .offer-badge {
    position: absolute; left: 110px; top: 503px; width: 174px; height: 174px; border-radius: 50%;
    background: var(--orange); border: 4px solid var(--badge-ring);
    display: flex; align-items: center; justify-content: center; text-align: center;
    font-weight: 800; font-size: 28px; line-height: 30px; color: var(--white);
  }
  .offer-title { position: absolute; left: 0; top: 107px; width: 395px; font-weight: 700; font-size: 21px; letter-spacing: 0.3px; }
  .offer-price { position: absolute; left: 76px; top: 140px; display: flex; align-items: center; }
  .offer-price .amount { font-weight: 800; font-size: 84px; line-height: 80px; letter-spacing: -1px; }
  .offer-price .amount sup { font-size: 30px; vertical-align: top; position: relative; top: 6px; margin-right: 2px; }
  .offer-price .regular {
    margin-left: 14px; padding-left: 14px; border-left: 1px solid rgba(255,255,255,0.7);
    font-weight: 600; font-size: 18px; line-height: 22px; text-align: left;
  }
  .offer-note {
    position: absolute; left: 48px; top: 237px; width: 298px;
    border-top: 1px solid rgba(255,255,255,0.8); border-bottom: 1px solid rgba(255,255,255,0.8);
    font-weight: 700; font-size: 20px; line-height: 36px;
  }
</style>
</head>
<body>
<main class="brochure">

  <section class="panel panel--about">
    <div class="about-photo" role="img" aria-label="Faint photo of a client standing in a cryosauna chamber"></div>
    <header class="about-head">
      <h1>ABOUT</h1>
      <h2>WHOLE BODY CRYOTHERAPY</h2>
    </header>
    <p class="about-body">With Whole Body Cryotherapy (WBC) the body is exposed to ultra-low temperatures, triggering a systemic anti-inflammatory response. This modality was first utilized in Japan in the early 1970’s by Dr. Hoshino to treat rheumatoid arthritis. Studies conducted over the last two decades have established WBC as a powerful treatment for inflammatory disorders and injuries. Professional athletes have discovered WBC as a powerful treatment to decrease recovery time, increase athletic performance, and boost the body’s metabolic rate.</p>

    <div class="pill pill--benefits">BENEFITS OF CRYOTHERAPY</div>
    <ul class="bullets bullets--benefits-a">
      <li>Pain Management</li><li>Injury Therapy</li><li>Rapid Recovery</li><li>Performance</li>
    </ul>
    <ul class="bullets bullets--benefits-b">
      <li>Metabolic Boost</li><li>Immunity Boost</li><li>Anti-Aging</li><li>Skin Rejuvenation</li>
    </ul>

    <div class="pill pill--applications">APPLICATIONS INCLUDE</div>
    <ul class="bullets bullets--applications">
      <li>Athletic performance</li><li>Postsurgical recovery</li><li>Musculoskeletal injures</li>
      <li>Rheumatoid arthritis</li><li>Weight management</li><li>Skin disorders</li>
      <li>Autoimmune disorders</li><li>Burn up to 800 calories</li><li>Better mood</li>
      <li>Sleep better</li><li>Increased metabolism</li>
    </ul>
  </section>

  <section class="panel panel--faq">
    <div class="faq-title"><h2>FAQs</h2><span></span></div>
    <article class="faq-item faq-item--work">
      <h3>HOW DOES WHOLE BODY<br>CRYOTHERAPY WORK?</h3>
      <p>Whole body skin exposure to ultra-low temperatures (-200°F to -260°F) triggers a systemic anti-inflammatory response that activates organs, muscles, joints, and skin to heal and repair themselves. The result is a dramatic increase in circulation, metabolism, tissue repair, detoxification, and immune function.</p>
    </article>
    <article class="faq-item faq-item--safe">
      <h3>IS IT SAFE?</h3>
      <p>Yes. Decades of studies from numerous institutions have shown it to be both safe and effective for a staggering variety of conditions and goals. The nitrogen being used to cool these chambers is the same nitrogen that makes up the air we breathe (actually 78% of it). Throughout treatment the client breathes room-air.</p>
    </article>
    <article class="faq-item faq-item--comfort">
      <h3>IS IT COMFORTABLE?</h3>
      <p>The treatment is of short duration (1½ - 2½ minutes), and the cold is ‘dry’, so it is very tolerable. Towards the end of treatment, you may get a ‘pins and needles’ sensation, which disappears immediately after treatment.</p>
    </article>
    <article class="faq-item faq-item--after">
      <h3>HOW DO I FEEL AFTER TREATMENT?</h3>
      <p>The brisk exhilaration causes your brain to release high amounts of endorphins, which make you feel good. Most people report feeling energetic and full of life. The buoyant effects from each session peak after many hours and may last for weeks.</p>
    </article>
  </section>

  <section class="panel panel--offer">
    <div class="tv-banner">
      <svg width="319" height="50" viewBox="0 0 319 50" aria-hidden="true">
        <polygon points="12,0 319,0 307,50 0,50" fill="#1a63b0"/>
      </svg>
      <span>AS SEEN ON TV!</span>
    </div>
    <div class="tv-logos">
      <div class="tv-name"><i></i>Health Hour</div>
      <div class="tv-name">Bright Mornings</div>
      <div class="tv-name">Vista Live</div>
    </div>
    <div class="tv-logos tv-logos--row2">
      <div class="tv-name">Game Desk</div>
      <div class="tv-name"><i></i>Star Beat</div>
      <div class="tv-name">Clinic Talk</div>
      <div class="tv-name">Metro Daily</div>
    </div>

    <div class="cryo-photo" role="img" aria-label="Photo of a smiling muscular man giving a thumbs up inside a cryosauna chamber"></div>

    <div class="offer-block">
      <div class="offer-title">INTRODUCTORY SESSION</div>
      <div class="offer-price">
        <div class="amount"><sup>$</sup>45</div>
        <div class="regular">Regular<br>Price $75</div>
      </div>
      <div class="offer-note">For new WBC clients only</div>
    </div>
    <div class="offer-badge">SPECIAL<br>OFFER</div>
  </section>

</main>
</body>
</html>
```